Kelmora Legal Business Card

I require a corporate business card for a new legal services business.

I do not have a logo, nor do I want one.

I require a clean, neat a professional card for a law firm.

Details:

Business Name: Kelmora Legal
Name: Debra Lindqvist
Title: Corporate Services Manager
Location: Office 14 (Top Floor), Toravel Business Centre, Quinlan Grove Street, Alotau CBD, Milne Bay Province.
Postal Address: PO Box 593, Alotau, 211, Milne Bay Province, Papua New Guinea.
Contact: T: +675 6418250, F: +675 6413362, M: +675 72915867, E: dlindqvist@kelmoraexample.com.pg.

I look forward to your design submissions.

Industry/Entity Type

Legal

```html
<!DOCTYPE html>
<html lang="en">
<head>
<meta charset="utf-8">
<title>Kelmora Legal Business Card</title>
<link rel="stylesheet" href="https://fonts.googleapis.com/css2?family=Archivo+Narrow:wght@400;500;700&family=Cinzel:wght@600&display=swap">
<style>
  :root {
    --orange: #ef7d1a;
    --charcoal: #3a3a3c;
    --card-white: #fbfbfb;
    --ink: #2b2b2b;
    --page: #ececec;
    --light-text: #ffffff;
  }
  * { margin: 0; padding: 0; box-sizing: border-box; }
  html, body { width: 1200px; height: 950px; overflow: hidden; }
  body {
    background: var(--page);
    font-family: "Archivo Narrow", "Arial Narrow", sans-serif;
    position: relative;
  }
  .card {
    position: absolute;
    left: 150px; top: 215px;
    width: 900px; height: 520px;
    background: var(--card-white);
    overflow: hidden;
    box-shadow: 0 2px 10px rgba(0,0,0,0.12);
  }
  .contact-panel {
    position: absolute; left: 430px; top: 0; right: 0; bottom: 0;
    background: var(--charcoal);
  }
  .accent-rule {
    position: absolute; left: 0; right: 0; top: 62px; height: 6px;
    background: var(--orange);
  }
  .title-band {
    position: absolute; left: 0; right: 0; top: 80px; height: 88px;
    background: var(--orange);
  }
  .firm-name {
    position: absolute; left: 48px; top: 100px;
    font-family: "Cinzel", "Copperplate", serif;
    font-weight: 600; font-size: 36px; letter-spacing: 3px;
    color: var(--light-text);
  }
  .person {
    position: absolute; left: 470px; top: 88px;
    color: var(--ink);
  }
  .person-name { font-weight: 700; font-size: 28px; line-height: 34px; }
  .person-title { font-weight: 400; font-size: 24px; line-height: 30px; }
  .contact-list {
    position: absolute; left: 470px; top: 200px;
    list-style: none; color: var(--light-text);
    font-size: 23px; line-height: 26px;
  }
  .contact-list li { display: flex; align-items: flex-start; margin-bottom: 9px; }
  .contact-icon { width: 22px; height: 22px; margin-right: 16px; margin-top: 2px; flex: none; }
  .postal { line-height: 27px; }
  .location {
    position: absolute; left: 50px; top: 300px; color: var(--ink);
  }
  .location-heading {
    display: inline-block;
    font-family: "Cinzel", "Copperplate", serif;
    font-weight: 600; font-size: 26px; letter-spacing: 2px;
    color: var(--orange);
    border-bottom: 3px solid var(--orange);
    padding-bottom: 1px; margin-bottom: 10px;
  }
  .location-address { font-style: normal; font-weight: 500; font-size: 23px; line-height: 29px; }
</style>
</head>
<body>
  <section class="card" aria-label="Kelmora Legal business card">
    <div class="contact-panel"></div>
    <div class="accent-rule"></div>
    <div class="title-band"></div>

    <h1 class="firm-name">Kelmora Legal</h1>

    <div class="person">
      <p class="person-name">Debra Lindqvist</p>
      <p class="person-title">Corporate Services Manager</p>
    </div>

    <ul class="contact-list">
      <li>
        <svg class="contact-icon" viewBox="0 0 22 22" aria-hidden="true">
          <circle cx="11" cy="11" r="11" fill="var(--orange)"/>
          <path d="M7 6.5c1-.8 1.6-.6 2 .2l.8 1.6c.3.6.1 1-.4 1.4l-.5.4c.6 1.3 1.6 2.3 2.9 2.9l.4-.5c.4-.5.8-.7 1.4-.4l1.6.8c.8.4 1 1 .2 2-1.2 1.4-3 1-5-.6-2-1.6-3.6-3.6-4-5.4-.2-1 .1-1.8.6-2.4z" fill="var(--charcoal)"/>
        </svg>
        <span>+675 6418250</span>
      </li>
      <li>
        <svg class="contact-icon" viewBox="0 0 22 22" aria-hidden="true">
          <circle cx="11" cy="11" r="11" fill="var(--orange)"/>
          <rect x="6" y="9" width="10" height="6" rx="1" fill="var(--charcoal)"/>
          <rect x="8" y="6" width="6" height="3" fill="var(--charcoal)"/>
        </svg>
        <span>+675 6413362</span>
      </li>
      <li>
        <svg class="contact-icon" viewBox="0 0 22 22" aria-hidden="true">
          <circle cx="11" cy="11" r="11" fill="var(--orange)"/>
          <rect x="8" y="5" width="6" height="12" rx="1" fill="var(--charcoal)"/>
          <rect x="9" y="6.5" width="4" height="7" fill="var(--orange)"/>
        </svg>
        <span>+675 72915867</span>
      </li>
      <li>
        <svg class="contact-icon" viewBox="0 0 22 22" aria-hidden="true">
          <rect x="1" y="5" width="20" height="13" fill="var(--orange)"/>
          <path d="M1 5l10 8 10-8" fill="none" stroke="var(--charcoal)" stroke-width="1.6"/>
        </svg>
        <span>dlindqvist@kelmoraexample.com.pg</span>
      </li>
      <li>
        <svg class="contact-icon" viewBox="0 0 22 22" aria-hidden="true">
          <path d="M11 1a7.5 7.5 0 0 0-7.5 7.5C3.5 14 11 21 11 21s7.5-7 7.5-12.5A7.5 7.5 0 0 0 11 1z" fill="var(--orange)"/>
          <circle cx="11" cy="8.5" r="3" fill="var(--charcoal)"/>
        </svg>
        <address class="postal" style="font-style:normal">PO Box 593, Alotau<br>211, Milne Bay Province<br>Papua New Guinea</address>
      </li>
    </ul>

    <div class="location">
      <h2 class="location-heading">Location</h2>
      <address class="location-address">
        Office 14 (Top Floor),<br>
        Toravel Business Centre,<br>
        Quinlan Grove Street,<br>
        Alotau CBD, Milne Bay Province
      </address>
    </div>
  </section>
</body>
</html>
```